Consultative Employee Benifits Firm Needs Business Card Design Project

We need a business card design for a new company based in Northern Virginia called "Telman Financial Services, LLC. We are both a wealth management advisory firm, as well as an employee benefits firm, which strives to provide superior creativity in employee benefits plan design and greater client and employee satisfaction. We are obsessed with service and follow up.

Our firm specializes in the areas of group health, life, dental, disability, voluntary benefits, Executive Benefits, HRA and HSA programs. We offer competitive employee benefit packages and pricing models for single or multi-state/multi location companies by maintaining preferred relationships with a large number of regional and national carriers.

Our firm also considers the many dimensions of your wealth through an integrated process we call wealth structuring — a comprehensive, dynamic approach to building, preserving, enjoying and transferring your wealth. And because we are often dealing with complex ownership structures and complicated, changing family dynamics, we bring the highest level of experience and creativity to managing your wealth. We work hard to help ensure that your legacy lasts by preparing your children for the financial challenges and opportunities that are headed their way.

Our final design should communicate an integrated approach to finanial safety and optimization
Updates

 Due to a few designers not accepting due to low budget, I have increased budget payout 19%. 

Project Deadline Extended
Reason: I have only heard from 12 designers. So, maybe I did not give the right amount of time to do the project. For the designers that have submitted their designs, thank you. I have seen three or four designs that I liked and might end up with one of them after it's all over, but I thought I would see between 20 - 25 before everything was over. Dan

Target Market(s)

Professionals; doctors, contractors, small to mid size business owners, ages 50 -65 with nert worth of 2MM

Industry/Entity Type

Financial

Requirements
Must have
• Telman Financial Services, LLC

Dan Telman
President
41957 Marwick Hollow Street
Quenford Glen, 20871

Office: 703 555-0184
Cell: 703 555-0127
Fax: 703 555-0163
Email: dantelman@quorvex.net
Should not have
• No pink or yellow colors.
No generic clipart (coins, dollar signs, money bags, graphs)

```html
<!DOCTYPE html>
<html lang="en">
<head>
<meta charset="utf-8">
<title>Telman Financial Services, LLC — Business Card</title>
<link rel="stylesheet" href="https://fonts.googleapis.com/css2?family=Jost:wght@400;500;600;700&display=swap">
<style>
  :root {
    --navy: #1e3577;
    --navy-deep: #14276a;
    --blue-glow: #2a5cb8;
    --ink: #111318;
    --grey: #7b7b7b;
    --paper: #ffffff;
    --backdrop: #ebe7e1;
  }
  * { box-sizing: border-box; margin: 0; padding: 0; }
  html, body {
    width: 1200px; height: 616px; overflow: hidden;
    background: var(--backdrop);
    font-family: "Jost", "Futura", sans-serif;
  }
  .canvas { position: relative; width: 1200px; height: 616px; }

  .card {
    position: absolute;
    width: 546px; height: 313px;
    border-radius: 22px;
    overflow: hidden;
    box-shadow: 3px 4px 8px rgba(0,0,0,.25);
  }

  /* Front */
  .card-front { left: 37px; top: 36px; background: var(--paper); }
  .front-wordmark {
    position: absolute; right: 42px; top: 34px;
    color: var(--navy); font-weight: 600; font-size: 25px; letter-spacing: .2px;
  }
  .holder { position: absolute; left: 42px; top: 144px; }
  .holder-name { color: var(--navy); font-weight: 600; font-size: 30px; line-height: 1.1; }
  .holder-title { color: var(--ink); font-weight: 500; font-size: 21px; line-height: 1.2; }
  .contact {
    position: absolute; left: 268px; top: 148px;
    border-left: 2px solid #9a9a9a;
    padding-left: 12px;
    font-size: 16px; line-height: 20.5px;
  }
  .contact-row { display: flex; }
  .contact-label { color: var(--grey); font-weight: 500; width: 54px; }
  .contact-value { color: var(--ink); font-weight: 500; }
  .address-band {
    position: absolute; left: 0; right: 0; top: 264px; height: 33px;
    background: var(--navy);
    color: #fff; font-weight: 500; font-size: 16.5px;
    padding-left: 42px; line-height: 33px;
  }

  /* Back */
  .card-back {
    left: 615px; top: 266px;
    background: radial-gradient(ellipse at 50% 42%, var(--blue-glow) 0%, var(--navy) 55%, var(--navy-deep) 100%);
    display: flex; align-items: center; justify-content: center;
  }
  .back-wordmark {
    color: #fff; font-weight: 600; font-size: 36px; letter-spacing: .3px;
    text-align: center;
  }
</style>
</head>
<body>
<main class="canvas">
  <section class="card card-front" aria-label="Business card front">
    <div class="front-wordmark">Telman Financial Services, LLC</div>
    <div class="holder">
      <div class="holder-name">Dan Telman</div>
      <div class="holder-title">President</div>
    </div>
    <div class="contact">
      <div class="contact-row"><span class="contact-label">Office:</span><span class="contact-value">703 555-0184</span></div>
      <div class="contact-row"><span class="contact-label">Cell:</span><span class="contact-value">703 555-0127</span></div>
      <div class="contact-row"><span class="contact-label">Fax:</span><span class="contact-value">703 555-0163</span></div>
      <div class="contact-row"><span class="contact-label">Email:</span><span class="contact-value">dantelman@quorvex.net</span></div>
    </div>
    <div class="address-band">41957 Marwick Hollow Street, Quenford Glen, VA 20871</div>
  </section>

  <section class="card card-back" aria-label="Business card back">
    <div class="back-wordmark">Telman Financial Services, LLC</div>
  </section>
</main>
</body>
</html>
```